New Turmel Business Card Design

We need a business card to match our new branding. The look should utilize the elements as attached here (Vector files & new exec overview are attached.) I really like 'organic' looking elements (e.g. an idea would be to have this printed on recycled paper stock). Thank you! Looking forward to seeing your designs.

Business

```html
<!DOCTYPE html>
<html lang="en">
<head>
<meta charset="UTF-8">
<title>Turmel Business Card</title>
<link rel="stylesheet" href="https://fonts.googleapis.com/css2?family=Questrial&family=Montserrat:wght@700&display=swap">
<style>
  :root {
    --page: #e4e5e7;
    --card-white: #ffffff;
    --brand-blue: #1b6db5;
    --brand-green: #86c142;
    --brand-green-light: #95c94d;
    --ink: #4a4a4a;
    --shadow: rgba(0,0,0,0.16);
  }
  * { box-sizing: border-box; margin: 0; padding: 0; }
  html, body { width: 1200px; height: 800px; overflow: hidden; }
  body {
    background: var(--page);
    font-family: "Questrial", sans-serif;
    display: flex;
    align-items: center;
    justify-content: center;
    gap: 50px;
  }
  .card {
    position: relative;
    width: 525px;
    height: 300px;
    box-shadow: 0 10px 24px var(--shadow);
    overflow: hidden;
  }
  /* Front */
  .card--front { background: var(--card-white); }
  .front__bands { position: absolute; left: 0; top: 0; }
  .front__wordmark {
    position: absolute;
    left: 44px; top: 38px;
    display: flex; align-items: center; gap: 12px;
    font-size: 60px;
    color: var(--brand-blue);
    letter-spacing: 1px;
    line-height: 1;
  }
  .front__dot {
    width: 18px; height: 18px; border-radius: 50%;
    background: var(--brand-green);
  }
  .front__web {
    position: absolute;
    left: 28px; top: 208px;
    font-size: 13px;
    color: var(--brand-blue);
    font-weight: bold;
    line-height: 1;
  }
  .contact {
    position: absolute;
    left: 300px; top: 110px;
    color: var(--ink);
    font-size: 12px;
    line-height: 1.3;
  }
  .contact__name {
    font-family: "Montserrat", sans-serif;
    font-weight: 700;
    font-size: 16px;
    color: var(--brand-blue);
  }
  .contact__title { font-size: 13px; margin-bottom: 6px; }
  .contact__line { display: flex; align-items: center; gap: 6px; }
  .contact__line svg { flex: none; }
  .contact__address { margin-top: 4px; }
  /* Back */
  .card--back {
    background: linear-gradient(135deg, var(--brand-green) 0%, var(--brand-green-light) 100%);
    display: flex; flex-direction: column; align-items: center; justify-content: center;
  }
  .back__wordmark {
    display: flex; align-items: center; gap: 12px;
    font-size: 60px; color: var(--card-white);
    letter-spacing: 1px; line-height: 1;
  }
  .back__dot { width: 18px; height: 18px; border-radius: 50%; background: var(--brand-blue); }
  .back__web { margin-top: 26px; font-size: 13px; color: var(--card-white); }
</style>
</head>
<body>
  <section class="card card--front" aria-label="Business card front">
    <svg class="front__bands" width="525" height="300" viewBox="0 0 525 300" aria-hidden="true">
      <polygon points="0,236 240,236 230,254 0,254" fill="var(--brand-blue)"/>
      <polygon points="238,258 525,258 525,278 228,278" fill="var(--brand-green)"/>
    </svg>
    <div class="front__wordmark"><span class="front__dot"></span>Turmel</div>
    <p class="front__web">www.turmelco.com</p>
    <div class="contact">
      <p class="contact__name">Daniel Okafor</p>
      <p class="contact__title">Principal</p>
      <p class="contact__line">
        <svg width="10" height="10" viewBox="0 0 10 10"><rect width="10" height="10" rx="2" fill="var(--brand-green)"/><path d="M3 2.5h1.3l.5 1.5-.8.6a4 4 0 0 0 1.4 1.4l.6-.8 1.5.5V7A1 1 0 0 1 6.5 8 4.5 4.5 0 0 1 2 3.5 1 1 0 0 1 3 2.5z" fill="#fff"/></svg>
        555.201.4478
      </p>
      <p class="contact__line">
        <svg width="10" height="10" viewBox="0 0 10 10"><rect width="10" height="10" rx="2" fill="var(--brand-green)"/><rect x="3.3" y="1.8" width="3.4" height="6.4" rx="0.6" fill="#fff"/></svg>
        555.309.2615
      </p>
      <p class="contact__line">
        <svg width="10" height="10" viewBox="0 0 10 10"><rect width="10" height="10" rx="2" fill="var(--brand-green)"/><rect x="2" y="3" width="6" height="4.2" fill="#fff"/><path d="M2 3l3 2.4L8 3" stroke="var(--brand-green)" stroke-width="0.7" fill="none"/></svg>
        daniel@turmelco.com
      </p>
      <p class="contact__address">48 Harlow Lane<br>Fairview, IL 60000</p>
    </div>
  </section>

  <section class="card card--back" aria-label="Business card back">
    <div class="back__wordmark"><span class="back__dot"></span>Turmel</div>
    <p class="back__web">www.turmelco.com</p>
  </section>
</body>
</html>
```